Quite your look: needs a logo design and a business card

The business name is called: Quite your look. It's all about fashion for everyone who needs to gain confidence and find his own style: Image Consultant, Personal Shopper. Here my Facebook fan page: https://www.examplebook.test/pages/Quite-your-look/804213967520431

I would like a smart logo & business card. The design has to be smart and long lasting. I like simplicity ("less is more"). The image needs to bring over seriousness and style. I target people from 35-65 years old. I would love to have smart warm colours like brown mole or anthracite, eventually with some berry or bordeaux red.

The copy is the following:
Quite your look
Daphne Volkers
Mobile: +27 71 436 02 59
eMail: volkers.daphne@mailbox.test
Cape Town

Target Market(s)

Core target group: 35-65 years old women; wealthy; living in Cape Town
Larger target group: South Africa; eventually men too

Industry/Entity Type

Business

```html
<!DOCTYPE html>
<html lang="en">
<head>
<meta charset="utf-8">
<title>Quite your look – Business Card</title>
<link rel="stylesheet" href="https://fonts.googleapis.com/css2?family=Alegreya:ital,wght@1,400&display=swap">
<style>
  :root {
    --berry: #992f5d;
    --berry-deep: #8e2a56;
    --amber: #cf7a45;
    --gold: #f8c52c;
    --paper: #ffffff;
    --backdrop: #ece8e6;
    --card-w: 900px;
    --card-h: 514px;
  }
  * { box-sizing: border-box; margin: 0; padding: 0; }
  html, body {
    width: 1200px; height: 1200px; overflow: hidden;
    background: var(--backdrop);
  }
  .canvas {
    width: 1200px; height: 1200px;
    display: flex; flex-direction: column;
    align-items: center; justify-content: center;
    gap: 60px;
  }
  .card {
    position: relative;
    width: var(--card-w); height: var(--card-h);
    overflow: hidden;
    box-shadow: 0 6px 18px rgba(0,0,0,0.12);
    font-family: "Alegreya", "Palatino Linotype", serif;
    font-style: italic;
  }
  /* Back side: contact details */
  .card--back { background: var(--paper); }
  .contact {
    position: absolute; left: 70px; top: 150px;
    list-style: none;
    color: var(--berry);
    font-size: 27px; line-height: 1.12;
  }
  /* Front side: name and tagline */
  .card--front {
    background: linear-gradient(180deg,
      var(--berry) 0%, var(--berry) 30%,
      var(--amber) 60%, var(--gold) 92%, var(--gold) 100%);
  }
  .brand-name {
    position: absolute; left: 250px; top: 190px;
    color: var(--paper);
    font-size: 58px; font-weight: 400;
    letter-spacing: 0.5px;
  }
  .person-name {
    position: absolute; left: 240px; top: 330px;
    color: var(--paper);
    font-size: 46px; font-weight: 400;
    letter-spacing: 0.5px;
  }
  .face-mark {
    position: absolute; right: 0; top: 0;
    width: 300px; height: 100%;
  }
</style>
</head>
<body>
<main class="canvas">
  <section class="card card--front" aria-label="Card front">
    <h1 class="brand-name">Quite your look</h1>
    <p class="person-name">Daphne Volkers</p>
    <svg class="face-mark" viewBox="0 0 300 514" role="img" aria-label="Line-art face illustration, golden strokes">
      <defs>
        <linearGradient id="front-mark-tone" x1="0" y1="0" x2="0" y2="1">
          <stop offset="0" stop-color="#f8c52c" stop-opacity="0.18"/>
          <stop offset="1" stop-color="#f8c52c" stop-opacity="0.35"/>
        </linearGradient>
      </defs>
      <rect x="0" y="0" width="300" height="514" fill="url(#front-mark-tone)"/>
    </svg>
  </section>

  <section class="card card--back" aria-label="Card back">
    <ul class="contact">
      <li>Quite your look</li>
      <li>Daphne Volkers</li>
      <li>Mobile: +27 71 436 02 59</li>
      <li>eMail: volkers.daphne@mailbox.test</li>
      <li>Cape Town</li>
    </ul>
    <svg class="face-mark" viewBox="0 0 300 514" role="img" aria-label="Line-art face illustration, berry strokes">
      <rect x="0" y="0" width="300" height="514" fill="#992f5d" fill-opacity="0.12"/>
    </svg>
  </section>
</main>
</body>
</html>
```